Clinic for cellulit and fat removal

Name of clinic :
Lumera
- Body & Health (this has to be written on the site.)
I need CMS for me to be able to make changes myself.
A webpage for woman searching for a solution to remove fat and cellulit.
The owner is a brazilian woman in Denmark, and want her sense of aestetic shines thru the website.
There needs to be a slide show on the landing page showing big sliding pictures, of the clinic and and the treatments.
The Cryolipolysis, is a treatment freezing fat and cellulit, and this treatment will be the Attraction of the clinic.
Needs These pages in a horisontal fasion. (written in Danish)
Lumera
Behandlinger
- Cryolipolysis
- Silkora
- Lymfemassage
- Tandrelia
- Copper Tide
Produkter
Priser
Kontakt

```html
<!DOCTYPE html>
<html lang="da">
<head>
<meta charset="utf-8">
<title>Lumera – Body &amp; Health</title>
<link rel="stylesheet" href="https://fonts.googleapis.com/css2?family=Oswald:wght@500;700&family=Poppins:wght@300;400;500;600&family=Cormorant+Garamond:ital,wght@0,500;1,500&display=swap">
<style>
:root{
  --magenta:#c0418e;
  --amber:#f9a23c;
  --orange:#fd7d3b;
  --lime:#a4cf38;
  --teal:#12b5c5;
  --navy:#2f3a4d;
  --ink:#1f1f1f;
  --grey:#8a8a8a;
  --line:#e7e7e7;
  --white:#ffffff;
}
*{box-sizing:border-box;margin:0;padding:0}
html,body{width:1200px;height:3905px;overflow:hidden}
body{font-family:"Poppins",Arial,sans-serif;color:var(--ink);background:var(--white);position:relative}
.page{position:relative;width:1200px;height:3905px}
section,header,footer{position:absolute;left:0;width:1200px}

.topbar{top:0;height:36px;background:var(--magenta);color:var(--white);font-size:11px}
.topbar .contacts{position:absolute;left:155px;top:11px;display:flex;gap:34px}
.topbar .social{position:absolute;right:150px;top:9px;display:flex;gap:8px}
.topbar .social i{width:18px;height:18px;border-radius:50%;background:var(--white);display:block}

.nav{top:36px;height:94px;background:var(--white)}
.brand{position:absolute;left:148px;top:18px;display:flex;align-items:center;gap:12px}
.brand .dot{width:26px;height:26px;border-radius:50%;background:var(--teal)}
.brand .name{font-size:32px;font-weight:400;color:var(--magenta);line-height:1}
.brand .sub{font-size:13px;color:var(--magenta);margin-top:4px}
.menu{position:absolute;right:150px;top:36px;display:flex;gap:42px;font-size:15px;color:var(--magenta)}

.hero{top:130px;height:651px}
.hero .photo{position:absolute;inset:0;background:linear-gradient(100deg,#5b7b4a 0%,#8ca07a 35%,#b9b3a6 60%,#7e8e70 100%)}
.hero .shade{position:absolute;inset:0;background:rgba(0,0,0,.22)}
.hero .kicker{position:absolute;top:318px;width:100%;text-align:center;font-family:"Cormorant Garamond",serif;font-size:22px;color:var(--white)}
.hero h1{position:absolute;top:345px;width:100%;text-align:center;font-family:"Oswald",sans-serif;font-weight:700;font-size:42px;color:var(--white);letter-spacing:.5px}
.hero .actions{position:absolute;top:415px;width:100%;display:flex;justify-content:center;gap:13px}
.btn{height:42px;border-radius:21px;padding:0 28px;font-size:14px;display:flex;align-items:center;color:var(--white)}
.btn.solid{background:var(--magenta)}
.btn.ghost{border:1.5px solid var(--white)}

.tiles{top:781px;height:229px;display:flex}
.tile{flex:1;color:var(--white);text-align:center;padding-top:64px}
.tile svg{display:block;margin:0 auto 14px}
.tile h3{font-size:19px;font-weight:600}
.tile small{display:block;font-size:8px;margin-top:12px;letter-spacing:1px;opacity:.85}
.tile.t1{background:var(--amber)}.tile.t2{background:var(--orange)}.tile.t3{background:var(--lime)}.tile.t4{background:var(--teal)}

.section-title{font-family:"Oswald",sans-serif;font-weight:700;font-size:33px;text-align:center;letter-spacing:.5px;color:#111}

.why{top:1040px;height:420px}
.why .section-title{position:absolute;top:16px;width:100%}
.why .lead{position:absolute;top:90px;left:210px;width:780px;text-align:center;font-size:12px;color:var(--grey);line-height:22px}
.why .cards{position:absolute;top:178px;left:120px;display:flex;gap:24px}
.why .card{width:304px;height:203px;position:relative;overflow:hidden}
.why .card .img{position:absolute;inset:0}
.why .card .cap{position:absolute;left:0;right:0;bottom:0;height:50px;background:rgba(25,25,25,.78);display:flex;align-items:center;color:var(--white);font-size:15px}
.why .card .cap i{width:50px;height:50px;background:var(--magenta);margin-right:16px;display:flex;align-items:center;justify-content:center}

.stories{top:1470px;height:400px}
.stories .section-title{position:absolute;top:22px;width:100%}
.stories .cards{position:absolute;top:102px;left:120px;display:flex;gap:30px}
.story{width:300px;height:224px;background:var(--white);box-shadow:0 2px 10px rgba(0,0,0,.1);padding:26px 26px}
.story .head{display:flex;align-items:center;gap:18px}
.story .avatar{width:58px;height:58px;border-radius:50%;background:linear-gradient(160deg,#d9b9a6,#8d6d5e);flex:none}
.story h4{font-size:16px;font-weight:400}
.story em{display:block;font-size:9px;color:var(--lime);margin-top:4px}
.story p{margin-top:28px;font-size:11.5px;line-height:22px;color:var(--grey)}
.dots{position:absolute;top:358px;left:573px;display:flex;gap:8px}
.dots i{width:10px;height:10px;border-radius:50%;background:#ddd}
.dots i:first-child{background:var(--lime)}

.team{top:1890px;height:421px}
.team .photo{position:absolute;inset:0;background:linear-gradient(90deg,#5a4a3c,#8a7a66 45%,#6b6155 75%,#4a3f36)}
.team .shade{position:absolute;inset:0;background:rgba(20,20,20,.55)}
.team .kicker{position:absolute;top:100px;width:100%;text-align:center;font-size:10px;color:var(--white);letter-spacing:1px}
.team h2{position:absolute;top:124px;width:100%;text-align:center;font-family:"Oswald",sans-serif;font-size:27px;color:var(--white)}
.team h2 span{color:var(--lime)}
.team .cols{position:absolute;top:203px;left:140px;display:flex;gap:50px}
.team .col{width:262px;display:flex;gap:14px;color:var(--white)}
.team .num{font-family:"Oswald",sans-serif;font-weight:700;font-size:50px;line-height:46px;border-bottom:4px solid var(--white);height:56px}
.team h5{font-size:14px;font-weight:400;margin-top:4px}
.team p{font-size:11px;line-height:19px;margin-top:16px}

.clients{top:2311px;height:430px}
.clients .section-title{position:absolute;top:38px;width:100%;font-size:26px}
.clients .lead{position:absolute;top:82px;left:400px;width:400px;text-align:center;font-size:11px;line-height:18px;color:#555}
.clients .card{position:absolute;top:151px;left:203px;width:794px;height:227px;border:1px solid var(--line);box-shadow:0 2px 10px rgba(0,0,0,.08);text-align:center}
.clients .card p{margin:56px auto 0;width:690px;font-size:11.5px;line-height:20px;color:#333}
.clients .avatar{width:48px;height:48px;border-radius:50%;margin:14px auto 0;background:linear-gradient(160deg,#d9b9a6,#7c5c50)}
.clients h4{font-size:15px;font-weight:500;margin-top:6px}
.clients small{font-size:9px;color:var(--grey)}
.arrow{position:absolute;top:2507px;width:30px;height:30px;border-radius:50%;border:1.5px solid var(--lime);display:flex;align-items:center;justify-content:center}

.subscribe{top:2741px;height:182px}
.subscribe .photo{position:absolute;inset:0;background:linear-gradient(90deg,#b84a8a,#c0418e 40%,#c95a9c)}
.subscribe h2{position:absolute;top:52px;width:100%;text-align:center;font-family:"Oswald",sans-serif;font-size:24px;color:var(--white)}
.subscribe form{position:absolute;top:96px;left:281px;width:635px;height:40px;background:var(--white);border-radius:20px;display:flex;align-items:center;justify-content:space-between;padding-left:22px;font-size:12px;color:#444}
.subscribe form span:last-child{height:100%;padding:0 26px;border-left:1px solid var(--line);display:flex;align-items:center;color:var(--magenta);font-weight:500}

.map{top:2923px;height:404px;background:linear-gradient(135deg,#e6e8dd,#d9dfd2 50%,#cfdbe6)}

.contact{top:3327px;height:252px;display:flex}
.contact div{text-align:center;color:var(--white);padding-top:74px}
.contact svg{display:block;margin:0 auto 24px}
.contact b{display:block;font-size:15px;font-weight:600}
.contact small{display:block;font-size:9px;letter-spacing:2px;margin-top:24px}
.contact .c1{width:396px;background:var(--orange)}
.contact .c2{width:395px;background:var(--lime)}
.contact .c3{width:409px;background:var(--teal)}

.footer{top:3579px;height:326px;background:var(--navy);text-align:center;color:var(--white)}
.footer .brand-foot{position:absolute;top:72px;width:100%;display:flex;justify-content:center;align-items:center;gap:14px}
.footer .brand-foot i{width:34px;height:34px;border-radius:50%;background:var(--teal)}
.footer .brand-foot b{font-size:56px;font-weight:400;color:var(--magenta);line-height:1}
.footer .tag{position:absolute;top:142px;width:100%;font-size:18px;color:var(--magenta)}
.footer nav{position:absolute;top:205px;width:100%;display:flex;justify-content:center;gap:32px;font-size:9px;letter-spacing:2px;color:#b7bdc9}
.footer .social{position:absolute;top:258px;width:100%;display:flex;justify-content:center;gap:46px}
.footer .social i{width:20px;height:20px;border-radius:50%;background:var(--white);display:block}
</style>
</head>
<body>
<div class="page">

<header class="topbar">
  <div class="contacts">
    <span>+45 31 22 48 90</span>
    <span>+45 31 22 48 91</span>
    <span>hello@lumera-clinic.dk</span>
  </div>
  <div class="social"><i></i><i></i><i></i><i></i><i></i><i></i></div>
</header>

<header class="nav">
  <div class="brand">
    <span class="dot"></span>
    <div><div class="name">Lumera</div><div class="sub">Body &amp; Health</div></div>
  </div>
  <nav class="menu"><span>Lumera</span><span>Behandlinger</span><span>Produkter</span><span>Priser</span><span>Kontakt</span></nav>
</header>

<section class="hero">
  <div class="photo" role="img" aria-label="Slideshow photo of the clinic and a cryolipolysis treatment"></div>
  <div class="shade"></div>
  <p class="kicker">Frys fedtet væk – helt uden kirurgi.</p>
  <h1>Velkommen til Lumera Body &amp; Health</h1>
  <div class="actions"><span class="btn solid">Læs mere</span><span class="btn ghost">Kontakt os</span></div>
</section>

<section class="tiles">
  <div class="tile t1">
    <svg width="40" height="40" viewBox="0 0 40 40" fill="none" stroke="#fff" stroke-width="2"><path d="M20 4v32M6 12l28 16M6 28l28-16M15 6l5 4 5-4M15 34l5-4 5 4"/></svg>
    <h3>Cryolipolysis</h3><small>LÆS MERE</small>
  </div>
  <div class="tile t2">
    <svg width="40" height="40" viewBox="0 0 40 40" fill="none" stroke="#fff" stroke-width="2"><path d="M12 4c0 10 4 12 4 18s-4 8-4 14M28 4c0 10-4 12-4 18s4 8 4 14M16 22h8"/></svg>
    <h3>Silkora</h3><small>LÆS MERE</small>
  </div>
  <div class="tile t3">
    <svg width="40" height="40" viewBox="0 0 40 40" fill="none" stroke="#fff" stroke-width="2"><path d="M8 24c4-8 8 4 12-4s8 4 12-4M8 32c4-8 8 4 12-4s8 4 12-4"/></svg>
    <h3>Lymfemassage</h3><small>LÆS MERE</small>
  </div>
  <div class="tile t4">
    <svg width="40" height="40" viewBox="0 0 40 40" fill="none" stroke="#fff" stroke-width="2"><rect x="10" y="12" width="20" height="24" rx="3"/><rect x="13" y="5" width="14" height="7"/><path d="M20 19v10M15 24h10"/></svg>
    <h3>Tandrelia</h3><small>LÆS MERE</small>
  </div>
</section>

<section class="why">
  <h2 class="section-title">HVORFOR VÆLGE LUMERA</h2>
  <p class="lead">Vi kombinerer brasiliansk sans for skønhed med dansk præcision, så du får en tryg, personlig behandling mod fedt og cellulite med synlige og varige resultater.</p>
  <div class="cards">
    <div class="card">
      <div class="img" role="img" aria-label="Photo of a cryolipolysis treatment in the clinic" style="background:linear-gradient(135deg,#7fb7c9,#cfe6ee)"></div>
      <div class="cap"><i><svg width="22" height="22" viewBox="0 0 22 22" fill="none" stroke="#fff" stroke-width="1.8"><path d="M11 2v18M3 6.5l16 9M3 15.5l16-9"/></svg></i>Cryolipolysis</div>
    </div>
    <div class="card">
      <div class="img" role="img" aria-label="Photo of a body treatment room" style="background:linear-gradient(135deg,#b98a7a,#e8cfc2 60%,#f1e6dc)"></div>
      <div class="cap"><i><svg width="22" height="22" viewBox="0 0 22 22" fill="none" stroke="#fff" stroke-width="1.8"><path d="M3 15h16v3H3zM5 15l3-8h5l2 8"/></svg></i>Copper Tide</div>
    </div>
    <div class="card">
      <div class="img" role="img" aria-label="Photo of a therapist consulting a client" style="background:linear-gradient(135deg,#9ec6dc,#e7c6a6 55%,#c78fae)"></div>
      <div class="cap"><i><svg width="22" height="22" viewBox="0 0 22 22" fill="none" stroke="#fff" stroke-width="1.8"><circle cx="11" cy="4" r="2"/><path d="M4 8h14M11 8v6l-4 6M11 14l4 6"/></svg></i>Personlig vejledning</div>
    </div>
  </div>
</section>

<section class="stories">
  <h2 class="section-title">SUCCESHISTORIER</h2>
  <div class="cards">
    <div class="story">
      <div class="head"><div class="avatar" role="img" aria-label="Client portrait"></div><div><h4>Marina Holst</h4><em>6 cm mindre om maven på 8 uger</em></div></div>
      <p>Efter to behandlinger med kuldeterapi kunne jeg se forskel. Personalet var varmt og rart, og jeg føler mig godt tilpas...</p>
    </div>
    <div class="story">
      <div class="head"><div class="avatar" role="img" aria-label="Client portrait"></div><div><h4>Oskar Brandt</h4><em>4 cm mindre om livet på 6 uger</em></div></div>
      <p>Jeg havde prøvet alt med kost og træning. Cryolipolysis fjernede endelig de sidste fedtdepoter, helt uden smerte og uden pause.</p>
    </div>
    <div class="story">
      <div class="head"><div class="avatar" role="img" aria-label="Client portrait"></div><div><h4>Julia Sørensen</h4><em>Glattere hud efter 10 uger</em></div></div>
      <p>Min cellulite på lårene er næsten væk. Lymfemassagen kombineret med kuldebehandling gjorde en stor forskel for mig...</p>
    </div>
  </div>
  <div class="dots"><i></i><i></i><i></i></div>
</section>

<section class="team">
  <div class="photo" role="img" aria-label="Photo of the clinic team at work"></div>
  <div class="shade"></div>
  <p class="kicker">MØD VORES TEAM</p>
  <h2>VENLIGE OG <span>PASSIONEREDE</span></h2>
  <div class="cols">
    <div class="col"><div class="num">01</div><div><h5>KONSULTATION</h5><p>Vi lytter til dine ønsker og laver en personlig plan for netop din krop.</p></div></div>
    <div class="col"><div class="num">02</div><div><h5>BEHANDLING</h5><p>Kulden fryser fedtcellerne, som kroppen selv udskiller over de næste uger.</p></div></div>
    <div class="col"><div class="num">03</div><div><h5>OPFØLGNING</h5><p>Vi måler dine resultater og guider dig til at bevare dem på lang sigt.</p></div></div>
  </div>
</section>

<section class="clients">
  <h2 class="section-title">DET SIGER VORES KUNDER</h2>
  <p class="lead">Ægte ord fra kvinder, der har fundet vejen tilbage til en krop, de trives i hver dag.</p>
  <div class="card">
    <svg style="position:absolute;top:22px;left:388px" width="18" height="14" viewBox="0 0 18 14" fill="#a4cf38"><path d="M0 14V7L4 0h3L5 7h3v7zM10 14V7l4-7h3l-2 7h3v7z"/></svg>
    <p>Jeg følte mig velkommen fra første besøg. Behandlingen var rolig og nem, og efter få uger kunne jeg se den forandring, jeg havde håbet på. Nu anbefaler jeg klinikken til alle mine veninder.</p>
    <div class="avatar" role="img" aria-label="Client portrait"></div>
    <h4>Camila Rocha</h4>
    <small>Kunde hos Lumera</small>
  </div>
</section>
<span class="arrow" style="left:209px"><svg width="12" height="12" viewBox="0 0 12 12" fill="none" stroke="#a4cf38" stroke-width="1.6"><path d="M8 2L4 6l4 4"/></svg></span>
<span class="arrow" style="left:956px"><svg width="12" height="12" viewBox="0 0 12 12" fill="none" stroke="#a4cf38" stroke-width="1.6"><path d="M4 2l4 4-4 4"/></svg></span>

<section class="subscribe">
  <div class="photo" role="img" aria-label="Magenta tinted photo of a smiling woman"></div>
  <h2>TILMELD DIG &amp; FÅ SKØNNE NYHEDER</h2>
  <form><span>Indtast din e-mail</span><span>TILMELD</span></form>
</section>

<section class="map" role="img" aria-label="Map showing the clinic location"></section>

<section class="contact">
  <div class="c1">
    <svg width="26" height="30" viewBox="0 0 26 30" fill="none" stroke="#fff" stroke-width="2"><rect x="6" y="2" width="14" height="26" rx="2"/><path d="M11 24h4"/></svg>
    <b>+45 70 20 14 88</b><small>TELEFON</small>
  </div>
  <div class="c2">
    <svg width="26" height="30" viewBox="0 0 26 30" fill="none" stroke="#fff" stroke-width="2"><path d="M13 28S3 17 3 11a10 10 0 0 1 20 0c0 6-10 17-10 17z"/><circle cx="13" cy="11" r="3.5"/></svg>
    <b>Vestergade 12, 1456 København K</b><small>ADRESSE</small>
  </div>
  <div class="c3">
    <svg width="30" height="30" viewBox="0 0 30 30" fill="none" stroke="#fff" stroke-width="2"><rect x="3" y="7" width="24" height="17"/><path d="M3 7l12 10 12-10"/></svg>
    <b>care@lumera-clinic.dk</b><small>E-MAIL</small>
  </div>
</section>

<footer class="footer">
  <div class="brand-foot"><i></i><b>Lumera</b></div>
  <div class="tag">Body &amp; Health</div>
  <nav><span>LUMERA</span><span>BEHANDLINGER</span><span>PRODUKTER</span><span>PRISER</span><span>KONTAKT</span></nav>
  <div class="social"><i></i><i></i><i></i><i></i><i></i></div>
</footer>

</div>
</body>
</html>
```